logo for security & safety training, education consultants
Marlow Advisory Nest Pte Ltd
Professional
LTC (RET) LIM BOON KEAT ROBERT MBA
DIRECTOR
47 JALAN TEMBUSIRA SINGAPORE 528806
robert@marlownest-example.com
www.marlownest-example.com
Perhaps some iso logo and same award logo in dummies

```html
<!DOCTYPE html>
<html lang="en">
<head>
<meta charset="utf-8">
<title>Marlow Advisory Nest – Business Card</title>
<link rel="stylesheet" href="https://fonts.googleapis.com/css2?family=Open+Sans:wght@400;600;800&display=swap">
<style>
  :root {
    --bg: #e9eaec;
    --card: #ffffff;
    --navy: #16172e;
    --blue: #2424d6;
    --ink: #2b2b33;
    --muted: #5b5b66;
    --rule: #121212;
  }
  * { box-sizing: border-box; margin: 0; padding: 0; }
  html, body {
    width: 1200px; height: 1002px; overflow: hidden;
    background: var(--bg);
    font-family: "Open Sans", Arial, sans-serif;
  }
  .sheet {
    position: relative; width: 1200px; height: 1002px;
    display: flex; flex-direction: column; align-items: center; justify-content: center; gap: 60px;
  }
  .card {
    position: relative; width: 700px; height: 400px;
    background: var(--card); border-radius: 22px; overflow: hidden;
    box-shadow: 0 10px 30px rgba(0,0,0,.12);
  }
  .brand { display: flex; align-items: center; gap: 14px; }
  .brand-dot { width: 30px; height: 30px; border-radius: 50%; background: var(--blue); }
  .brand-name { font-weight: 800; color: var(--navy); letter-spacing: 1px; line-height: 1; }

  /* back */
  .card--back { display: flex; align-items: center; justify-content: center; }
  .card--back .brand-name { font-size: 64px; }
  .card--back .brand-dot { width: 44px; height: 44px; }

  /* front */
  .card--front .brand { position: absolute; left: 44px; top: 44px; }
  .card--front .brand-name { font-size: 44px; }
  .contact-list {
    position: absolute; left: 48px; top: 110px; list-style: none;
    font-size: 12px; color: var(--ink); line-height: 19px;
  }
  .contact-list li { display: flex; align-items: center; gap: 10px; }
  .contact-icon { width: 14px; height: 14px; flex: none; }
  .contact-list .indent { padding-left: 24px; }
  .band { position: absolute; left: 0; top: 0; width: 700px; height: 400px; }
  .holder {
    position: absolute; right: 44px; top: 264px; text-align: right; color: var(--ink);
  }
  .holder-name { font-size: 13px; font-weight: 600; letter-spacing: .5px; }
  .holder-role { font-size: 10px; letter-spacing: 2px; color: var(--muted); margin-top: 4px; }
  .web {
    position: absolute; right: 60px; bottom: 14px; color: #fff;
    font-size: 14px; letter-spacing: 2px;
  }
</style>
</head>
<body>
<main class="sheet">
  <section class="card card--back" aria-label="Card back">
    <div class="brand">
      <span class="brand-dot"></span>
      <span class="brand-name">MARLOW</span>
    </div>
  </section>

  <section class="card card--front" aria-label="Card front">
    <svg class="band" viewBox="0 0 700 400" aria-hidden="true">
      <path d="M0 300 L0 400 L700 400 L700 360 L310 360 C255 360 225 350 200 330 C165 304 130 300 60 300 Z" fill="var(--blue)"/>
      <path d="M0 288 C110 288 155 298 190 320 C222 340 250 348 310 348 L700 348" fill="none" stroke="var(--rule)" stroke-width="4"/>
    </svg>

    <div class="brand">
      <span class="brand-dot"></span>
      <span class="brand-name">MARLOW</span>
    </div>

    <ul class="contact-list">
      <li><svg class="contact-icon" viewBox="0 0 14 14"><circle cx="7" cy="7" r="7" fill="var(--blue)"/><path d="M7 3.2a2.4 2.4 0 0 1 2.4 2.4C9.4 7.6 7 10.8 7 10.8S4.6 7.6 4.6 5.6A2.4 2.4 0 0 1 7 3.2z" fill="#fff"/></svg>47 JALAN TEMBUSIRA</li>
      <li class="indent">SINGAPORE 528806</li>
      <li><svg class="contact-icon" viewBox="0 0 14 14"><circle cx="7" cy="7" r="7" fill="var(--blue)"/><path d="M4.5 3.5l1.6 1.6-.8 1.1a5 5 0 0 0 2.5 2.5l1.1-.8 1.6 1.6-1 1C6.5 10.5 3.5 7.5 3.5 4.5z" fill="#fff"/></svg>+65 6100 2200</li>
      <li><svg class="contact-icon" viewBox="0 0 14 14"><circle cx="7" cy="7" r="7" fill="var(--blue)"/><path d="M4.5 3.5l1.6 1.6-.8 1.1a5 5 0 0 0 2.5 2.5l1.1-.8 1.6 1.6-1 1C6.5 10.5 3.5 7.5 3.5 4.5z" fill="#fff"/></svg>+65 9100 3300</li>
      <li><svg class="contact-icon" viewBox="0 0 14 14"><circle cx="7" cy="7" r="7" fill="var(--blue)"/><rect x="3.5" y="4.5" width="7" height="5" fill="#fff"/></svg>+65 6100 4400</li>
      <li><svg class="contact-icon" viewBox="0 0 14 14"><circle cx="7" cy="7" r="7" fill="var(--blue)"/><rect x="3.5" y="4.5" width="7" height="5" fill="#fff"/><path d="M3.5 4.5L7 7.5 10.5 4.5" stroke="var(--blue)" fill="none"/></svg>robert@marlownest-example.com</li>
      <li><svg class="contact-icon" viewBox="0 0 14 14"><circle cx="7" cy="7" r="7" fill="var(--blue)"/><circle cx="7" cy="7" r="3.5" fill="none" stroke="#fff"/><path d="M3.5 7h7" stroke="#fff"/></svg>www.marlownest-example.com</li>
    </ul>

    <div class="holder">
      <p class="holder-name">LTC (RET) LIM BOON KEAT ROBERT MBA</p>
      <p class="holder-role">DIRECTOR</p>
    </div>

    <p class="web">www.marlownest-example.com</p>
  </section>
</main>
</body>
</html>
```